Unique business card design

We are looking for a design that reflects our unique social media and online marketing agency "Kestrel Media". We are a young agency with a focus on speakers, coaches and trainers. In other words, we support people who want to do good with their work and help other people live a happier, more successful and fulfilling life, reach as many people as possible with their work and thus have an influence. Our values are: sustainability, creating added value, individuality, proactivity. We want our clients to feel comfortable with us and that's why the relationship with them is very important to us. We want every customer to become a lifelong friend of the company. Most of our clients are premium coaches, meaning they are in the higher priced segment and expect seriousness, professionalism and quality. All of these things should reflect our business card as well. I look forward to feedback. Best regards, Tomas Wylander

```html
<!DOCTYPE html>
<html lang="en">
<head>
<meta charset="utf-8">
<title>Kestrel Media — Business Card</title>
<link href="https://fonts.googleapis.com/css2?family=Michroma&family=Arimo:wght@400&display=swap" rel="stylesheet">
<style>
  :root {
    --bg: #d9dadd;
    --card: #ffffff;
    --navy: #26287a;
    --indigo: #3a3d9e;
    --blue: #1f86cf;
    --ink: #2b2d5e;
    --icon: #2f3d8f;
  }
  * { box-sizing: border-box; margin: 0; padding: 0; }
  html, body { width: 1200px; height: 932px; overflow: hidden; }
  body {
    background: var(--bg);
    display: flex;
    align-items: center;
    justify-content: center;
    gap: 80px;
  }
  .card {
    width: 340px;
    height: 595px;
    background: var(--card);
    border-radius: 26px;
    box-shadow: 0 8px 24px rgba(0,0,0,0.18);
    position: relative;
    overflow: hidden;
  }
  .brand {
    position: absolute;
    left: 44px;
    top: 120px;
    display: flex;
    flex-direction: column;
    gap: 12px;
  }
  .brand-row { display: flex; align-items: center; gap: 14px; }
  .brand-square {
    width: 54px; height: 54px;
    background: var(--blue);
    flex: none;
  }
  .brand-name {
    font-family: "Michroma", sans-serif;
    font-size: 22px;
    line-height: 1.2;
    color: var(--navy);
    letter-spacing: 0.5px;
  }
  .brand-tagline {
    font-family: "Michroma", sans-serif;
    font-size: 12.5px;
    color: var(--indigo);
    letter-spacing: 0.3px;
  }
  .card-back .brand { top: 240px; }
  .person {
    position: absolute;
    left: 44px;
    top: 350px;
  }
  .person-name {
    font-family: "Michroma", sans-serif;
    font-size: 21px;
    color: var(--navy);
    letter-spacing: 1px;
  }
  .person-title {
    font-family: "Michroma", sans-serif;
    font-size: 15px;
    color: var(--indigo);
    margin-top: 4px;
  }
  .address, .contact {
    font-family: "Arimo", sans-serif;
    font-size: 13.5px;
    color: var(--ink);
    line-height: 1.45;
  }
  .address { margin-top: 18px; }
  .contact { margin-top: 16px; list-style: none; }
  .contact li { display: flex; align-items: center; gap: 10px; margin-bottom: 6px; }
  .contact-icon { width: 20px; height: 20px; flex: none; }
</style>
</head>
<body>
  <article class="card card-front">
    <div class="brand">
      <div class="brand-row">
        <span class="brand-square"></span>
        <span class="brand-name">Kestrel Media</span>
      </div>
      <span class="brand-tagline">Online Marketing Services</span>
    </div>
    <div class="person">
      <h1 class="person-name">TOMAS WYLANDER</h1>
      <p class="person-title">President</p>
      <p class="address">310, 48 Harbour Ln NW<br>Calgary, AB, T3K 2P4</p>
      <ul class="contact">
        <li>
          <svg class="contact-icon" viewBox="0 0 20 20" aria-hidden="true">
            <rect width="20" height="20" rx="4" fill="var(--icon)"/>
            <path d="M6 5h2.5l1 3-1.5 1a7 7 0 0 0 3 3l1-1.5 3 1V14a1.5 1.5 0 0 1-1.5 1.5A9 9 0 0 1 4.5 6.5 1.5 1.5 0 0 1 6 5z" fill="#fff"/>
          </svg>
          <span>403-555-0148</span>
        </li>
        <li>
          <svg class="contact-icon" viewBox="0 0 20 20" aria-hidden="true">
            <rect width="20" height="20" rx="4" fill="var(--icon)"/>
            <rect x="4" y="6" width="12" height="8.5" fill="none" stroke="#fff" stroke-width="1.3"/>
            <path d="M4 6l6 5 6-5" fill="none" stroke="#fff" stroke-width="1.3"/>
          </svg>
          <span>tomas@kestrelmedia.com</span>
        </li>
        <li>
          <svg class="contact-icon" viewBox="0 0 20 20" aria-hidden="true">
            <rect width="20" height="20" rx="4" fill="var(--icon)"/>
            <circle cx="10" cy="10" r="5.5" fill="none" stroke="#fff" stroke-width="1.2"/>
            <ellipse cx="10" cy="10" rx="2.4" ry="5.5" fill="none" stroke="#fff" stroke-width="1"/>
            <path d="M4.5 10h11" stroke="#fff" stroke-width="1"/>
          </svg>
          <span>www.kestrelmedia.com</span>
        </li>
      </ul>
    </div>
  </article>

  <article class="card card-back">
    <div class="brand">
      <div class="brand-row">
        <span class="brand-square"></span>
        <span class="brand-name">Kestrel Media</span>
      </div>
      <span class="brand-tagline">Online Marketing Services</span>
    </div>
  </article>
</body>
</html>
```